Business Card for Quillmark Ledger - A cannabis publication for executives.

I'd like some business cards for Quillmark Ledger. The logo is done (great job!) and I need a card design I will use with PRINTLY. I made it a short project to allow time for printing before an event. These will be standard sized cards (final artwork size 3.66" x 2.16" at 300dpi) with a final card size of 3.5" x 2.0". (See PRINTLY.com if you need more info.) I might try rounded corners but am not sure yet. I think the design will work okay with rounded.

Quillmark Ledger will be a bi-weekly publication for the cannabis industry. It is targeted to investors and industry executives, not consumers or pot smokers. So our market is more B2B. However I am open to creativity and making the card something people remark on.

My contact for card:

Dana Merrow
Founder/CEO
dana@quillmarkledger.example

2740 Harlow Avenue
Boston MA 02135
(617)555-0194

Target Market(s)

Executives, Industry people and investors in the Cannabis sector.

Contact Information for Business Card

PRINTLY does do double sided and the second side can be the same or different images. Only one side is required but use of the second side would be a bonus.

Font styles to use
Serif
Sans Serif
Decorative

Colors

Designer to choose colors to be used in the design.

Requirements
Must have
• Logo, contact info
Nice to have
• Style and design to make the card stand out in a crowd.

```html
<!DOCTYPE html>
<html lang="en">
<head>
<meta charset="utf-8">
<title>Quillmark Ledger — Business Card</title>
<link rel="stylesheet" href="https://fonts.googleapis.com/css2?family=Lato:wght@400;700&display=swap">
<style>
  :root {
    --page-bg: #e6ebf1;
    --card-white: #ffffff;
    --brand-blue: #2360a8;
    --brand-blue-deep: #1b4f8f;
    --brand-green: #5e9b2f;
    --contact-text: #e8eef6;
    --name-text: #f3d9c8;
  }
  * { box-sizing: border-box; margin: 0; padding: 0; }
  html, body { width: 1200px; height: 900px; overflow: hidden; }
  body {
    background: var(--page-bg);
    font-family: "Lato", Arial, sans-serif;
    position: relative;
  }
  .business-card {
    position: absolute;
    left: 180px;
    top: 210px;
    width: 840px;
    height: 480px;
    border-radius: 16px;
    overflow: hidden;
    background: var(--card-white);
    box-shadow: 0 12px 30px rgba(30, 50, 80, 0.18);
  }
  .card-wave {
    position: absolute;
    inset: 0;
    width: 840px;
    height: 480px;
  }
  .brand-lockup {
    position: absolute;
    left: 46px;
    top: 58px;
    display: flex;
    align-items: center;
    gap: 26px;
  }
  .brand-square {
    width: 72px;
    height: 72px;
    background: var(--brand-green);
  }
  .brand-name {
    font-size: 58px;
    font-weight: 700;
    color: var(--brand-blue);
    letter-spacing: -0.5px;
    line-height: 1;
  }
  .person {
    position: absolute;
    left: 40px;
    top: 375px;
  }
  .person-name {
    font-size: 29px;
    font-weight: 700;
    color: var(--name-text);
    letter-spacing: 0.3px;
  }
  .person-title {
    font-size: 21px;
    color: var(--contact-text);
    margin-top: 4px;
  }
  .contact-list {
    position: absolute;
    right: 40px;
    top: 286px;
    list-style: none;
    text-align: right;
    color: var(--contact-text);
    font-size: 20px;
    line-height: 28px;
  }
  .contact-list li {
    display: flex;
    justify-content: flex-end;
    align-items: center;
    gap: 10px;
  }
  .contact-icon { width: 17px; height: 17px; flex: none; }
  .address {
    position: absolute;
    right: 64px;
    top: 391px;
    font-style: normal;
    text-align: right;
    color: var(--contact-text);
    font-size: 20px;
    line-height: 28px;
  }
</style>
</head>
<body>
  <article class="business-card">
    <svg class="card-wave" viewBox="0 0 840 480" aria-hidden="true">
      <defs>
        <linearGradient id="waveBlue" x1="0" y1="0" x2="1" y2="1">
          <stop offset="0" stop-color="#2b6ab4"/>
          <stop offset="1" stop-color="#1b4f8f"/>
        </linearGradient>
      </defs>
      <path d="M0 318 C 280 318, 620 300, 840 140 L 840 480 L 0 480 Z" fill="url(#waveBlue)"/>
      <path d="M0 318 C 280 318, 620 300, 840 140" fill="none" stroke="#5e9b2f" stroke-width="6"/>
      <path d="M0 324 C 280 324, 624 306, 840 148" fill="none" stroke="#ffffff" stroke-width="2" opacity="0.6"/>
    </svg>

    <div class="brand-lockup">
      <span class="brand-square"></span>
      <span class="brand-name">Quillmark Ledger</span>
    </div>

    <div class="person">
      <p class="person-name">Dana Merrow</p>
      <p class="person-title">Founder/CEO</p>
    </div>

    <ul class="contact-list">
      <li>(617)555-0194
        <svg class="contact-icon" viewBox="0 0 24 24" aria-hidden="true"><path fill="currentColor" d="M6.6 10.8a15.1 15.1 0 0 0 6.6 6.6l2.2-2.2c.3-.3.7-.4 1-.2 1.1.4 2.3.6 3.6.6.6 0 1 .4 1 1V20c0 .6-.4 1-1 1C10.6 21 3 13.4 3 4c0-.6.4-1 1-1h3.5c.6 0 1 .4 1 1 0 1.3.2 2.5.6 3.6.1.3 0 .7-.2 1l-2.3 2.2z"/></svg>
      </li>
      <li>dana@quillmarkledger.example
        <svg class="contact-icon" viewBox="0 0 24 24" aria-hidden="true"><rect x="2" y="5" width="20" height="14" rx="1.5" fill="currentColor"/><path d="M3 6l9 7 9-7" fill="none" stroke="#1f5699" stroke-width="1.8"/></svg>
      </li>
      <li>www.quillmarkledger.example
        <svg class="contact-icon" viewBox="0 0 24 24" aria-hidden="true"><g fill="none" stroke="currentColor" stroke-width="1.8"><circle cx="12" cy="12" r="9"/><ellipse cx="12" cy="12" rx="4" ry="9"/><path d="M3 12h18M5 7h14M5 17h14"/></g></svg>
      </li>
    </ul>

    <address class="address">
      2740 Harlow Avenue<br>
      Boston MA 02135
    </address>
  </article>
</body>
</html>
```